Bring Days 4 Wonder campaign: promoting kids play in the UK - Website Redesign

Bring Days 4 Wonder is a national UK campaign that promotes the value of play for children. The current website is live at http://www.bringdays4wonder.co.uk. This website has been live for 4 years and now needs to be redesigned. The target audience is parents of young children up to the age of 12.

The current site was designed with a series of old adverts in mind. Here is an example of an old advert: http://vidshare.example/k3RwqLmZ8Tb

Criticisms of existing site:
The design represented the adverts too closely. The result was a website that mirrors the adverts rather than complements them.
The color scheme is too dark.
Text-heavy pages (e.g. http://www.bringdays4wonder.co.uk/fun.php) are dull and not FUN!

New site
We have recently had a series of new video adverts produced:
advert 1: http://vidshare.example/Hq2vXnB7eJs
advert 2: http://vidshare.example/Wm9cTpR4uLd
advert 3: http://vidshare.example/Zg5sKbN1oVe

The new site should be cleaner and brighter than the existing site, possibly with a white background using graphics, fonts and advert characters (see attached character graphics files) to add the element of fun and play.

The homepage should include:
1. Bring Days for Wonder logo (attached)
2. Social Media links (visible on all pages of the site) – Facebook, Twitter, YouTube
3. Link to the BringDays4Wonder app page of the site (visible on all pages)
4. Image/video placeholder that the user can scroll through, view full-size images and play videos.
5. Text area to hold approximately 100 words describing the purpose of the campaign
6. Site footer to contain the same information as on the existing site along with the Northern Game & Craft Guild logo (attached)

Site structure:
One change to the site structure… the “Brought to you by” menu item will be removed from the top-level menu.

General:
Some pages on the existing site are quite text-heavy, we would like to break up text on these pages in some way. Graphical division of paragraphs, use of advert characters?

Please note that all attached graphics file are the property of the Northern Game & Craft Guild and must only be used for the purpose of this project.

```html
<!DOCTYPE html>
<html lang="en">
<head>
<meta charset="utf-8">
<title>Bring Days 4 Wonder</title>
<link rel="stylesheet" href="https://fonts.googleapis.com/css2?family=Cabin+Sketch:wght@400;700&family=Gochi+Hand&family=Dancing+Script&family=Open+Sans:wght@400&display=swap">
<style>
:root{
  --brand-red:#d42e2f;
  --footer-red:#a71c2d;
  --nav-active:#f7d21b;
  --white:#ffffff;
  --headline-pink:#e8506a;
  --headline-blue:#22a7de;
  --tagline-green:#3cb371;
  --quote-purple:#6b3f8f;
  --heading-purple:#6a3d9a;
  --body-grey:#555555;
  --play-grey:#666666;
  --app-purple:#7b3fa0;
}
*{margin:0;padding:0;box-sizing:border-box}
html,body{width:1200px;height:1126px;overflow:hidden;background:var(--white)}
body{position:relative;font-family:'Open Sans',sans-serif}

.site-header{position:absolute;left:0;top:0;width:1200px;height:130px;background:var(--brand-red)}
.brand{position:absolute;left:36px;top:40px;display:flex;align-items:center;gap:10px;
  font-family:'Gochi Hand',cursive;font-size:26px;line-height:26px;color:var(--white);width:170px}
.brand-dot{width:22px;height:22px;border-radius:50%;background:var(--nav-active);flex:none}
.main-nav{position:absolute;top:72px;left:0;width:1200px;height:40px}
.main-nav a{position:absolute;font-family:'Gochi Hand',cursive;font-size:26px;color:var(--white);text-decoration:none;white-space:nowrap}
.main-nav a.active{color:var(--nav-active);border-bottom:3px solid var(--nav-active);padding-bottom:6px}
.social{position:absolute;top:30px;left:982px;display:flex;gap:22px}
.social span{display:block;width:24px;height:24px;border-radius:50%;background:var(--white)}
.app-link{position:absolute;left:1114px;top:22px;width:48px;height:76px;border-radius:8px;background:var(--app-purple)}
.app-link::after{content:"";position:absolute;left:6px;top:12px;width:36px;height:48px;background:var(--white)}

.hero{position:absolute;left:0;top:130px;width:1200px;height:640px;
  background:linear-gradient(135deg,#ffffff 0%,#f4f4f4 60%,#ececec 100%);overflow:hidden}
.hero-character{position:absolute;left:36px;top:74px;width:384px;height:504px;border-radius:120px 120px 30px 30px;
  background:linear-gradient(180deg,#f2d6bd 0%,#e24a50 45%,#8fd6c3 80%,#f3f3f3 100%);opacity:.85}
.hero-landscape{position:absolute;left:0;top:0}
.headline{position:absolute;left:456px;top:38px;font-family:'Cabin Sketch',sans-serif;font-weight:700;
  font-size:122px;line-height:118px;color:var(--headline-pink)}
.headline .blue{color:var(--headline-blue)}
.tagline{position:absolute;right:474px;top:486px;text-align:right;font-family:'Gochi Hand',cursive;
  font-size:25px;line-height:34px;color:var(--tagline-green)}
.quote{position:absolute;left:946px;top:318px;width:230px;font-family:'Dancing Script',cursive;
  font-size:20px;line-height:46px;color:var(--quote-purple)}
.play-button{position:absolute;left:926px;top:48px}

.intro{position:absolute;left:102px;top:806px;width:996px;text-align:center}
.intro h1{font-family:'Cabin Sketch',sans-serif;font-weight:700;font-size:42px;letter-spacing:4px;color:var(--heading-purple);margin-bottom:14px}
.intro p{font-size:12.6px;line-height:20px;color:var(--body-grey);margin-bottom:19px}

.site-footer{position:absolute;left:0;top:1030px;width:1200px;height:96px;background:var(--footer-red);
  font-family:'Gochi Hand',cursive;color:var(--white);font-size:17px;line-height:24px}
.site-footer span{position:absolute;white-space:nowrap}
.site-footer .address{left:36px;top:36px}
.site-footer .disclaimer{left:328px;top:36px}
.site-footer .guild{left:586px;top:14px;width:100px;text-align:center;font-size:15px;line-height:22px;white-space:normal}
.site-footer .copyright{right:38px;top:36px}
</style>
</head>
<body>
<header class="site-header">
  <div class="brand"><span class="brand-dot"></span>Bring Days for Wonder</div>
  <nav class="main-nav">
    <a class="active" href="#" style="left:317px">Play Right Now</a>
    <a href="#" style="left:520px">Get Involved</a>
    <a href="#" style="left:690px">Why Play</a>
    <a href="#" style="left:829px">Fun Forever</a>
    <a href="#" style="left:995px">Resources</a>
  </nav>
  <div class="social" aria-label="Social media links"><span></span><span></span><span></span></div>
  <a class="app-link" href="#" aria-label="BringDays4Wonder app"></a>
</header>

<section class="hero">
  <div class="hero-character" role="img" aria-label="Illustrated girl in a red cardigan holding a stick"></div>
  <svg class="hero-landscape" width="1200" height="640" role="img" aria-label="Sunny landscape with four children holding hands on a green hill">
    <defs>
      <linearGradient id="sky" x1="0" y1="0" x2="0" y2="1">
        <stop offset="0" stop-color="#d8eef7"/>
        <stop offset=".7" stop-color="#eaf6fb"/>
        <stop offset=".78" stop-color="#9fd25a"/>
        <stop offset="1" stop-color="#6fb43a"/>
      </linearGradient>
    </defs>
    <polygon points="678,640 1086,0 1200,0 1200,640" fill="url(#sky)"/>
  </svg>
  <div class="headline">Bring<br>Days 4<br><span class="blue">Wonder</span></div>
  <svg class="play-button" width="100" height="150" aria-label="Play video">
    <circle cx="42" cy="42" r="38" fill="#fff" stroke="var(--play-grey)" stroke-width="8"/>
    <polygon points="34,28 34,56 56,42" fill="var(--play-grey)"/>
    <path d="M8,140 C40,150 62,120 56,96" fill="none" stroke="#f2c318" stroke-width="3"/>
    <path d="M46,106 L56,94 L64,108" fill="none" stroke="#f2c318" stroke-width="3"/>
  </svg>
  <p class="quote">It is widely recognised that play is essential for a developing child</p>
  <p class="tagline">in physical<br>activity and the link with body image.</p>
</section>

<main class="intro">
  <h1>Play Therapy</h1>
  <p>As an intrinsic part of childhood toys play many different roles: from comforters to imaginary friends; tools for cooperative play to exploratory construction. They can also be of immense use in educational and therapeutic environments where play therapy is an integral part of helping children cope with difficult or challenging situations.</p>
  <p>We thought you might be interested in this aspect of play so we asked the experts at RCH (Riverside Children's Hospital) and SafeSteps to discover how appropriate toys can really help children who may be facing a change in family circumstances, a medical procedure or long-term health issues.</p>
</main>

<footer class="site-footer">
  <span class="address">27 Larkfield Lane, Leeds, LS6 2QD</span>
  <span class="disclaimer">Click here to read the disclaimer</span>
  <span class="guild">Northern Game<br>&amp; Craft<br>Guild</span>
  <span class="copyright">© 2014 Northern Game &amp; Craft Guild Ltd. All Rights Reserved</span>
</footer>
</body>
</html>
```